Lena Corvell Business Card

I need a business card that reflects my current website: itslenacorvell.example and screenshot attached. If we keep the color scheme of the site and sample card below that would be ideal. The business card should include the information on the attached sample cards.

Industry/Entity Type

Business

```html
<!DOCTYPE html>
<html lang="en">
<head>
<meta charset="utf-8">
<title>Lena Corvell Business Card</title>
<link rel="stylesheet" href="https://fonts.googleapis.com/css2?family=Open+Sans:wght@300;400&display=swap">
<style>
  :root {
    --backdrop: #e4e4e2;
    --card: #ffffff;
    --teal: #6bb8a8;
    --ink: #1a1a1a;
    --muted: #4a4a4a;
    --shadow: rgba(0, 0, 0, 0.18);
  }
  html, body {
    margin: 0;
    padding: 0;
    width: 1200px;
    height: 821px;
    overflow: hidden;
    background: var(--backdrop);
    font-family: "Open Sans", Arial, sans-serif;
  }
  .business-card {
    position: absolute;
    left: 180px;
    top: 170px;
    width: 840px;
    height: 480px;
    background: var(--card);
    box-shadow: 0 14px 36px var(--shadow);
    overflow: hidden;
  }
  .accent-band {
    position: absolute;
    left: 190px;
    top: 92px;
    width: 470px;
    height: 96px;
    background: var(--teal);
  }
  .wordmark {
    position: absolute;
    left: 70px;
    top: 108px;
    font-weight: 400;
    color: var(--ink);
    white-space: nowrap;
    line-height: 1;
  }
  .wordmark-prefix {
    font-size: 30px;
    margin-right: 14px;
  }
  .wordmark-name {
    font-size: 62px;
  }
  .tagline {
    position: absolute;
    left: 140px;
    top: 214px;
    font-size: 15px;
    font-weight: 300;
    color: var(--muted);
    letter-spacing: 0.2px;
  }
  .contact {
    position: absolute;
    right: 56px;
    top: 250px;
    text-align: right;
    font-weight: 300;
    color: var(--ink);
    line-height: 1.3;
  }
  .contact-name {
    font-size: 24px;
    color: var(--teal);
    letter-spacing: 1px;
    margin-bottom: 4px;
  }
  .contact-line {
    font-size: 20px;
  }
  .social-line {
    font-size: 20px;
    display: flex;
    justify-content: flex-end;
    align-items: center;
    gap: 8px;
  }
  .social-dot {
    width: 12px;
    height: 12px;
    background: var(--teal);
    display: inline-block;
  }
  .social-divider {
    color: var(--teal);
  }
</style>
</head>
<body>
  <section class="business-card" aria-label="Lena Corvell business card">
    <div class="accent-band"></div>
    <div class="wordmark">
      <span class="wordmark-prefix">i am</span><span class="wordmark-name">Lena Corvell</span>
    </div>
    <p class="tagline">Brand Curator | Digital Storyteller | Social Entrepreneur</p>
    <div class="contact">
      <div class="contact-name">LENA CORVELL</div>
      <div class="contact-line">me@lenacorvell.example</div>
      <div class="contact-line">240.555.0142</div>
      <div class="social-line">
        <span class="social-dot"></span><span class="social-divider">|</span>
        <span class="social-dot"></span><span class="social-divider">|</span>
        <span class="social-dot"></span>
        <span>@itslenacorvell</span>
      </div>
      <div class="contact-line">www.itslenacorvell.example</div>
    </div>
  </section>
</body>
</html>
```